Small animal veterinary clinic needs a new web site design

We need a new web site design for Harlowe Veterinary Clinic. The clinic performs medicine, surgery, and wellness care for cats and dogs. We have been in business for over 50 years so we want to project stability, reliability, class, elegance, and professionalism. We also want to convey that we have modern facilities and services and perform high quality medicine.
The current web site has been in place for many years and looks stale but for reference it is at http://www.harlowevetcare.example. We will be re-writing most of the content and looking to add additional pages, videos, downloadable documents (forms, brochures, marketing materials, etc.) The new owners prefer a more classy, modern look. Some vet clinic sites we like are http://pintrelpaws.example and http://corvalanimalcare.example. We like a nice, clean, fresh, interactive interface.
Our new logo is attached. We want the color scheme of the web site to be complementary to the colors in the logo, especially the blue and green. The purple color of the text should just be used for accent. Upon request and if necessary, I can supply the Adobe Illustrator source file for the logo.
We are looking for a set of page designs - a great, eye-catching home page and 2-3 content page layouts we can use to create content pages with our own text and other content. Navigation design is very important as well. Again, we can fill in the content of the navigation links but I would like a nice, easy-to-use, logical navigation design. If you want some content or navigation links to use as reference during your design phase, feel free to pull whatever content or navigation you want from our existing web site. I am not looking for just images, I would like actual page files - HTML, CSS, etc.
Thanks and good luck!
Target Market(s)
We cater to pet owners across a wide age range. Socio-economic status of our customers is middle class and above. We do not target price shoppers.
Industry/Entity Type
Veterinary
Colors
Designer to choose colors to be used in the design.
Requirements
Must have
- Must look professional, clean, and modern. We are looking for simple but elegant design and navigation. 1 home page design, 2-3 content page designs delivered with code (HTML & CSS).
Nice to have
- When HTML/CSS is delivered, it would be awesome if it were mobile ready as well.
Should not have
- Colors that are too bold. Layout that is too complex.

```html
<!DOCTYPE html>
<html lang="en">
<head>
<meta charset="utf-8">
<title>Harlowe Veterinary Clinic</title>
<link rel="stylesheet" href="https://fonts.googleapis.com/css2?family=Open+Sans:wght@400;600&family=Didact+Gothic&display=swap">
<style>
:root{
  --teal:#1f8a94;
  --sky:#1aa0d8;
  --nav-a:#2b8a9a;
  --nav-b:#1d5f86;
  --active:#8cc6a2;
  --ink:#333;
  --muted:#7a7a7a;
  --card:#fff;
  --btn:#3b3f47;
  --dark:#2c2c2c;
  --footer:#383838;
  --fb:#3b5c8f;
  --tw:#3ea3d8;
  --rss:#e0b43a;
  --gp:#c9433a;
}
*{box-sizing:border-box;margin:0;padding:0}
html,body{width:1200px;height:2400px;overflow:hidden;background:#fff}
body{position:relative;font-family:"Open Sans",sans-serif;color:var(--ink)}
.abs{position:absolute}

/* header */
.brand{left:8px;top:20px;width:150px;height:120px;display:flex;flex-direction:column;align-items:center;justify-content:center;gap:8px}
.brand-mark{width:22px;height:22px;border-radius:50%;background:var(--teal)}
.brand-name{font-size:19px;font-weight:600;color:var(--teal);text-align:center;line-height:1.2}
.social{display:flex;gap:20px}
.social span{display:block;width:44px;height:44px}
.s-fb{background:var(--fb)}.s-tw{background:var(--tw)}.s-rss{background:var(--rss)}.s-gp{background:var(--gp)}
.social.top{left:944px;top:16px}
.appt{left:956px;top:70px;font-size:20px;color:var(--teal)}
.phone{left:976px;top:96px;font-size:23px;color:var(--teal);letter-spacing:1px}

/* nav */
.nav{left:0;top:156px;width:1200px;height:84px;background:linear-gradient(90deg,var(--nav-a),var(--nav-b) 45%,#3c8fa8 75%,var(--nav-a))}
.nav-active{left:234px;top:154px;width:222px;height:118px;background:var(--active);opacity:.85}
.nav-link{top:180px;font-size:24px;color:#fff;letter-spacing:.5px}

/* hero */
.hero-pets{left:0;top:252px;width:392px;height:344px;background:radial-gradient(ellipse at 40% 55%,#c9863e 0%,#b98b5c 35%,#d9d3c8 60%,#fff 78%)}
.hero-title{left:430px;top:296px;width:720px;text-align:center;font-family:"Didact Gothic",sans-serif;font-size:74px;line-height:80px;color:var(--sky);letter-spacing:-2px}

/* features band */
.band{left:0;top:596px;width:1200px;height:410px;background:radial-gradient(ellipse at 50% 10%,#cfe8e0 0%,#7fbcc0 30%,#3a97ad 60%,#2a7fa0 100%)}
.card{background:var(--card);text-align:center}
.card h2{font-weight:400;font-size:36px;margin-top:40px;letter-spacing:1px;color:#333}
.card p{font-size:16px;line-height:23px;color:var(--muted);margin-top:18px}
.more{width:50px;height:48px;background:var(--btn);display:flex;align-items:center;justify-content:center}

/* staff */
.avatar{width:76px;height:76px;border-radius:50%;background:radial-gradient(circle,#6d6a62,#a9a49a)}
.staff-name{font-size:25px;color:#555}
.staff-role{font-size:16px;color:var(--muted);line-height:20px}
.staff-text{font-size:17px;line-height:23px;color:var(--muted);width:310px}
.read{width:194px;height:62px;background:var(--btn);border:2px solid #d8e4c6;color:#fff;font-size:17px;line-height:20px;text-align:center;padding-top:9px;letter-spacing:1px}

/* story */
.story{left:0;top:1466px;width:1200px;height:458px;background:linear-gradient(100deg,#2784b6 0%,#1c6ea6 40%,#0f5a98 70%,#1d86c2 100%)}
.story h2{left:60px;top:1520px;font-weight:400;font-size:34px;color:#fff;letter-spacing:1px}
.video{left:60px;top:1588px;width:338px;height:182px;background:linear-gradient(90deg,#8b8f87,#5b6a72 60%,#3a4650)}
.story-cap{left:60px;top:1784px;font-size:22px;color:#3d6f8c}
.story-sub{left:60px;top:1820px;font-size:16px;color:#7fa9c4}

/* about */
.about{left:0;top:1924px;width:1200px;height:310px;background:radial-gradient(ellipse at 50% 40%,#6b6b6b,#3a3a3a 55%,#222 100%)}
.about h2{left:0;top:1998px;width:1200px;text-align:center;font-weight:400;font-size:31px;color:#fff;letter-spacing:1px}
.about p{left:60px;top:2062px;width:1080px;font-size:16.5px;line-height:24px;color:#f0f0f0}

/* footer */
.footer{left:0;top:2234px;width:1200px;height:166px;background:var(--footer)}
.foot-links{left:60px;top:2300px;font-size:17px;line-height:22px;color:#fff}
.social.bottom{left:886px;top:2290px}
.totop{left:1128px;top:2304px;width:52px;height:48px;background:#fff;display:flex;align-items:center;justify-content:center}
</style>
</head>
<body>
<header>
  <div class="abs brand"><span class="brand-mark"></span><span class="brand-name">HARLOWE<br>Veterinary Clinic</span></div>
  <div class="abs social top"><span class="s-fb"></span><span class="s-tw"></span><span class="s-rss"></span><span class="s-gp"></span></div>
  <div class="abs appt">Request an Appointment</div>
  <div class="abs phone">+1 800 555 0142</div>
</header>

<nav>
  <div class="abs nav"></div>
  <div class="abs nav-active"></div>
  <span class="abs nav-link" style="left:254px">OUR PRACTICES</span>
  <span class="abs nav-link" style="left:478px">OUR STAFF</span>
  <span class="abs nav-link" style="left:646px">SERVICES</span>
  <span class="abs nav-link" style="left:798px">CONTACT US</span>
</nav>

<section>
  <div class="abs hero-pets" role="img" aria-label="Photo of a golden dog lying beside a tabby cat"></div>
  <h1 class="abs hero-title" style="font-weight:400">Your Pet Will Love you<br>For This<br>Forever.</h1>
</section>

<section>
  <div class="abs band"></div>
  <div class="abs card" style="left:60px;top:660px;width:326px;height:216px">
    <h2>LATEST NEWS</h2><p>We Offer Pet Portals!</p>
  </div>
  <div class="abs more" style="left:336px;top:828px"><svg width="12" height="14" viewBox="0 0 12 14"><path d="M3 2l6 5-6 5" fill="none" stroke="#fff" stroke-width="2"/></svg></div>
  <div class="abs card" style="left:422px;top:660px;width:326px;height:262px">
    <h2>LINKS</h2><p>Crestline Nutrition<br>Please visit our website for<br>Boarding and Grooming</p>
  </div>
  <div class="abs more" style="left:698px;top:874px"><svg width="12" height="14" viewBox="0 0 12 14"><path d="M3 2l6 5-6 5" fill="none" stroke="#fff" stroke-width="2"/></svg></div>
  <div class="abs card" style="left:786px;top:660px;width:326px;height:286px">
    <h2>CARE GUIDES</h2><p>Exercising Your Dog<br>Feline Obesity<br>Radiography<br>Spaying or Neutering Your Pet</p>
  </div>
  <div class="abs more" style="left:1062px;top:898px"><svg width="12" height="14" viewBox="0 0 12 14"><path d="M3 2l6 5-6 5" fill="none" stroke="#fff" stroke-width="2"/></svg></div>
</section>

<section>
  <div class="abs avatar" style="left:60px;top:1126px" role="img" aria-label="Staff portrait"></div>
  <div class="abs staff-name" style="left:222px;top:1124px">PERSPICIATIS</div>
  <div class="abs staff-role" style="left:222px;top:1170px">TOTAM REM<br>APERIAM</div>
  <div class="abs staff-text" style="left:60px;top:1228px">Eaque ipsa quae ab illo inventore veritatis et quasi architecto beatae vitae dicta sunt explicabo.</div>
  <div class="abs read" style="left:90px;top:1332px">READ<br>MORE</div>

  <div class="abs avatar" style="left:424px;top:1126px" role="img" aria-label="Staff portrait"></div>
  <div class="abs staff-name" style="left:586px;top:1124px">PERSPICIATIS</div>
  <div class="abs staff-role" style="left:586px;top:1170px">TOTAM REM<br>APERIAM</div>
  <div class="abs staff-text" style="left:424px;top:1228px">Eaque ipsa quae ab illo inventore veritatis et quasi architecto beatae vitae dicta sunt explicabo.</div>
  <div class="abs read" style="left:454px;top:1332px">READ<br>MORE</div>

  <div class="abs avatar" style="left:788px;top:1126px" role="img" aria-label="Staff portrait"></div>
  <div class="abs staff-name" style="left:950px;top:1124px">PERSPICIATIS</div>
  <div class="abs staff-role" style="left:950px;top:1170px">TOTAM REM<br>APERIAM</div>
  <div class="abs staff-text" style="left:788px;top:1228px">Eaque ipsa quae ab illo inventore veritatis et quasi architecto beatae vitae dicta sunt explicabo.</div>
  <div class="abs read" style="left:818px;top:1332px">READ<br>MORE</div>
</section>

<section>
  <div class="abs story"></div>
  <h2 class="abs" style="left:60px;top:1520px;font-weight:400;font-size:34px;color:#fff;letter-spacing:1px">MARK AND LENA OSTROW SHARE THEIR STORY</h2>
  <div class="abs video" role="img" aria-label="Video still of two clinic clients talking"></div>
  <svg class="abs" style="left:206px;top:1656px" width="46" height="46" viewBox="0 0 46 46"><circle cx="23" cy="23" r="20" fill="none" stroke="#fff" stroke-width="3" opacity=".8"/><path d="M18 14l13 9-13 9z" fill="#fff" opacity=".8"/></svg>
  <div class="abs" style="left:358px;top:1728px;width:40px;height:40px;background:#333;display:flex;align-items:center;justify-content:center"><svg width="18" height="18" viewBox="0 0 18 18"><circle cx="7" cy="7" r="5" fill="none" stroke="#fff" stroke-width="2"/><path d="M11 11l5 5" stroke="#fff" stroke-width="2"/></svg></div>
  <div class="abs story-cap">PERSPICIATIS</div>
  <div class="abs story-sub">TOTAM REM APERIAM</div>
</section>

<section>
  <div class="abs about" role="img" aria-label="Blurred photo of the clinic interior"></div>
  <h2 class="abs" style="left:0;top:1998px;width:1200px;text-align:center;font-weight:400;font-size:31px;color:#fff;letter-spacing:1px">WHAT WE DO</h2>
  <p class="abs" style="left:60px;top:2062px;width:1080px;font-size:16.5px;line-height:24px;color:#f0f0f0">Harlowe Veterinary Clinic is a full-service veterinary medical hospital, located in Brookhaven, SC. The professional and courteous staff at Harlowe Veterinary Clinic seeks to provide the best possible medical care, surgical care and dental care for their highly-valued patients. We are committed to promoting responsible pet ownership, preventative health care and health-related educational opportunities for our clients.</p>
</section>

<footer>
  <div class="abs footer"></div>
  <div class="abs foot-links">Site Map HOME| ABOUT| NEWS/EVENTS| FAQS| CONTACT|<br>Copyright © 2014 All rights reserved.</div>
  <div class="abs social bottom"><span class="s-fb"></span><span class="s-tw"></span><span class="s-rss"></span><span class="s-gp"></span></div>
  <div class="abs totop"><svg width="10" height="14" viewBox="0 0 10 14"><path d="M5 13V2M1 6l4-4 4 4" fill="none" stroke="#333" stroke-width="2"/></svg></div>
</footer>
</body>
</html>
```